Trifold flyer for our dental clinic (The Bright Harbor Clinic)

The goal of this project is to design a trifold flyer for our dental clinic (The Bright Harbor Clinic). The winning design is expected to be creative, artistic and coherent with our logo.
Updates

Designs look the same

Target Market(s)

Young generation with dental need.

Industry/Entity Type

Dental Clinic

Font styles to use
Sans Serif

Colors
0355a3
85acd3
85cae6
0592cd
00a990
86cfc6
cedeed
cee9f5
cfeae6

Requirements
Must have
• See the attached sketch for content arrangement.

```html
<!DOCTYPE html>
<html lang="en">
<head>
<meta charset="utf-8">
<title>Bright Harbor Clinic – Trifold Flyer</title>
<link href="https://fonts.googleapis.com/css2?family=Lato:ital,wght@0,300;0,400;0,700;0,900;1,300;1,400&display=swap" rel="stylesheet">
<style>
:root{
  --navy:#0355a3;
  --deep:#073d86;
  --ink:#0a2f6b;
  --sky:#0592cd;
  --bright:#1ba0dc;
  --pale:#85cae6;
  --mist:#cee9f5;
  --frost:#e9f4fb;
  --steel:#85acd3;
  --bar:#141a24;
  --stage:#5c626b;
  --white:#ffffff;
  --text:#2b2f36;
}
*{margin:0;padding:0;box-sizing:border-box}
html,body{width:1200px;height:3390px;overflow:hidden}
body{background:var(--stage);font-family:'Lato',sans-serif;color:var(--text);position:relative}
.spread{position:absolute;left:60px;width:1085px;height:842px;display:flex;box-shadow:0 6px 20px rgba(0,0,0,.35)}
.spread.inside{top:1559px}
.spread.outside{top:2458px;height:845px}
.panel{position:relative;height:100%;overflow:hidden}
.p1{width:360px}.p2{width:355px}.p3{width:370px}
.abs{position:absolute}
.center{left:0;right:0;text-align:center}
.footer{position:absolute;left:0;right:0;bottom:18px;height:30px;background:var(--bar);color:var(--white);font-size:14px;letter-spacing:2.4px;text-align:center;line-height:30px;z-index:2}
.outside .footer{bottom:0}
.footer-under{position:absolute;left:0;right:0;bottom:0;height:18px;background:var(--pale)}
.waves{position:absolute;left:0;width:100%}
.photo{position:absolute;border-radius:50%;border:5px solid var(--white);box-shadow:0 2px 6px rgba(0,0,0,.25);background:radial-gradient(circle at 50% 40%,#d9b7a0,#5b4a44 70%)}

/* team panel */
.team{background:linear-gradient(180deg,var(--frost),#f4f9fd)}
.heading{font-size:24px;font-weight:400;letter-spacing:.5px}
.team .heading{top:34px;color:var(--sky)}
.dash{width:44px;height:2px;background:var(--ink);margin:8px auto 0}
.member-name{font-size:14.5px;color:var(--text);text-transform:uppercase}
.member-role{font-size:11px;color:#555;line-height:1.25}
.callnow{top:720px;font-size:19px;color:var(--ink);line-height:1.2}
.callnow b{display:block;font-size:36px;font-weight:900;color:var(--ink);line-height:1.1}

/* reviews panel */
.reviews{background:linear-gradient(160deg,var(--deep),var(--navy) 55%,#0a4da0);color:var(--white)}
.reviews .heading{top:34px;color:var(--pale)}
.quote{font-family:Georgia,serif;font-size:110px;color:rgba(133,202,230,.45);line-height:1;font-weight:700}
.review{left:24px;right:26px;font-size:10.8px;font-style:italic;line-height:1.33;text-align:justify;font-weight:300}
.reviewer{left:24px;right:26px;font-size:11.5px;font-weight:700;display:flex;justify-content:space-between}
.stars{color:#f5c518;letter-spacing:1px;font-size:14px}
.contact{left:63px;top:510px;width:230px;height:230px;border-radius:50%;background:var(--white);border:7px solid var(--mist);box-shadow:0 0 0 2px var(--pale);text-align:center;color:var(--text);padding-top:40px}
.contact h3{font-weight:400;font-size:24px;color:var(--sky);margin-bottom:10px}
.contact p{font-size:11.5px;line-height:1.5}

/* cover panel */
.cover{background:var(--white)}
.brand{font-size:22px;font-weight:700;color:var(--sky);letter-spacing:.5px;display:flex;flex-direction:column;align-items:center;gap:14px}
.brand-mark{width:46px;height:46px;background:var(--pale)}
.hero{position:absolute;left:0;right:0;top:195px;height:395px;background:linear-gradient(135deg,#e8eef3,#b8c9d8 55%,#7d9ab5)}
.offer-band{position:absolute;left:0;right:0;top:570px;bottom:0;background:linear-gradient(180deg,var(--navy),var(--deep))}
.offer{left:44px;top:650px;color:var(--white)}
.offer h2{font-size:27px;font-weight:700;margin-left:28px;margin-bottom:14px}
.offer p{font-size:21px;font-weight:300;font-style:italic;line-height:1.35;color:var(--mist)}
.offer p b{font-style:normal;font-weight:700;color:var(--white)}

/* outside promos panel */
.promos{background:var(--white)}
.section-title{display:flex;align-items:center;justify-content:center;gap:8px;font-size:22px;font-weight:700;color:var(--sky)}
.section-title i{display:inline-block;width:44px;height:22px;background:var(--pale)}
.rule{height:2px;background:#bbb;margin:6px auto 0;width:160px}
.promo-box{left:40px;right:40px;border:2px solid var(--navy);text-align:center;color:var(--ink);padding:8px 6px}
.promo-box .lead{font-size:20px}
.promo-box .lead b{color:var(--sky)}
.promo-box .sub{font-size:15px}
.promo-box .big{font-size:24px;font-weight:900;color:var(--navy)}
.services{left:20px;top:650px;list-style:none;font-size:12.5px;font-weight:700;color:var(--navy);line-height:1.3}
.services li::before{content:"\2714";color:var(--sky);margin-right:5px;font-size:10px}
.team-photo{left:190px;top:650px;width:168px;height:135px;background:linear-gradient(135deg,#f6c2d9,#f7e27a 50%,#8fd3f0)}

/* plan panel */
.plan{background:linear-gradient(180deg,var(--deep),var(--navy));color:var(--white)}
.boxed{left:20px;right:20px;border:2px solid var(--pale);text-align:center;font-size:22px;line-height:1.2}
.note{font-size:13.5px;line-height:1.3}
.plan-head{font-size:19px;font-weight:700;color:var(--pale)}
.row{left:28px;right:18px;display:flex;align-items:center}
.row .items{width:148px;font-size:13.5px;line-height:1.2}
.row .brace{font-size:48px;font-weight:300;line-height:1;margin-right:14px}
.row .save{font-size:21px;font-weight:700;line-height:1.15}
.fee{left:20px;right:20px;top:697px;height:90px;background:var(--bright);text-align:center;font-size:19px;line-height:1.25;padding-top:6px}

/* info panel */
.info{background:var(--white);text-align:center}
.hours-title{top:228px;font-size:29px;font-weight:900;color:var(--sky);line-height:1.05}
.hours{top:304px;font-size:20px;line-height:1.3;color:var(--text)}
.hours b{font-weight:400}
.calltoday{top:388px;font-size:28px;font-weight:900;color:var(--sky);line-height:1.1}
.calltoday span{display:block;color:var(--ink);font-size:28px}
.addr{top:478px;font-size:14.5px;font-weight:700;color:var(--text);line-height:1.4}
.site{top:533px;font-size:19px;font-weight:700;color:var(--sky)}
.map{left:39px;width:283px;top:577px;height:178px;border:4px solid #ddd;border-radius:6px;background:linear-gradient(135deg,#eef1f3,#dfe4e8)}
</style>
</head>
<body>

<section class="spread inside">
  <div class="panel p1 team">
    <h2 class="abs center heading">OUR TEAM<div class="dash"></div></h2>
    <div class="photo" role="img" aria-label="Portrait of Dr. Mara Ellison" style="left:115px;top:95px;width:130px;height:130px"></div>
    <div class="abs center" style="top:243px"><div class="member-name">Mara Ellison, DMD, MS</div><div class="member-role">Board Certified Orthodontist</div></div>
    <div class="photo" role="img" aria-label="Portrait of Dr. Stefan R. Whitcombe" style="left:115px;top:290px;width:130px;height:130px"></div>
    <div class="abs center" style="top:438px"><div class="member-name">Stefan R. Whitcombe, DMD</div><div class="member-role">Board Certified Pediatric Dentist<br>Board Certified Orthodontist</div></div>
    <div class="photo" role="img" aria-label="Portrait of Dr. Lena Farouk" style="left:115px;top:500px;width:130px;height:130px"></div>
    <div class="abs center" style="top:645px"><div class="member-name">Dr. Lena Farouk, DMD</div><div class="member-role">General Dentist</div></div>
    <svg class="waves" style="top:660px" width="360" height="182" viewBox="0 0 360 182" preserveAspectRatio="none">
      <path d="M0 40 C120 -10 250 90 360 60 L360 182 L0 182Z" fill="var(--pale)"/>
      <path d="M0 30 C120 -20 250 80 360 50 L360 62 C250 94 120 4 0 48Z" fill="var(--navy)"/>
      <path d="M0 54 C120 14 250 100 360 72 L360 182 L0 182Z" fill="var(--mist)"/>
    </svg>
    <div class="abs center callnow">CALL US NOW<b>555-014-2277</b></div>
    <div class="footer">www.brightharborclinic.com</div>
    <div class="footer-under"></div>
  </div>

  <div class="panel p2 reviews">
    <div class="abs quote" style="left:22px;top:20px">&ldquo;</div>
    <h2 class="abs center heading">REVIEWS</h2>
    <p class="abs review" style="top:96px">This place is the best dentist ever. I've had a lot of other dentists but none quite like this place! She's so funny and she shakes it all the time (like a maraca). We are always having a good time, laughing, joking, and just all around having fun in this office! Not to mention it's so clean and state of the art. The dentists there were always helping and explaining the process and made me very comfortable.</p>
    <div class="abs reviewer" style="top:216px"><span>COLIN FERRIS (7/14/2017)</span><span class="stars">★★★★★</span></div>
    <p class="abs review" style="top:254px">I LOVE everyone at this office!! Dr. Ellison is the best of the best. The office staff are always courteous and kind, even kept an eye on my granddaughter who was watching TV while I was being seen. They are professional, nice, outgoing, friendly – just what every office strives to be – they have it all!!</p>
    <div class="abs reviewer" style="top:342px"><span>DORA STRATTON (2/19/2018)</span><span class="stars">★★★★★</span></div>
    <p class="abs review" style="top:384px">I have been coming to see Dr. Ellison for over a year now. She has been nothing but amazing! Her staff is wonderful and makes you feel like you're family from the moment you walk in the door. I cannot say enough good things about her and her office!</p>
    <div class="abs reviewer" style="top:476px"><span>KARA ROWLAND (8/23/2019)</span><span class="stars">★★★★★</span></div>
    <div class="abs quote" style="right:24px;top:488px">&rdquo;</div>
    <div class="abs contact">
      <h3>Contact Us</h3>
      <p>240 Harbor Lane Suite<br>12 Bayview, MA 01999<br>555-014-2277<br>555-014-3861<br>hello@brightharborclinic.com</p>
    </div>
    <div class="footer">www.brightharborclinic.com</div>
    <div class="footer-under" style="background:var(--navy)"></div>
  </div>

  <div class="panel p3 cover">
    <div class="abs center brand" style="top:48px"><span class="brand-mark"></span>THE BRIGHT HARBOR CLINIC</div>
    <div class="hero" role="img" aria-label="Photo of a smiling young couple"></div>
    <svg class="waves" style="top:170px" width="370" height="40" viewBox="0 0 370 40" preserveAspectRatio="none">
      <path d="M0 0 C120 40 250 40 370 10 L370 40 L0 40Z" fill="#e8eef3"/>
      <path d="M0 0 C120 36 250 36 370 6 L370 14 C250 42 120 42 0 8Z" fill="var(--sky)"/>
    </svg>
    <div class="offer-band"></div>
    <svg class="waves" style="top:540px" width="370" height="80" viewBox="0 0 370 80" preserveAspectRatio="none">
      <path d="M0 70 C120 20 250 10 370 40 L370 80 L0 80Z" fill="var(--navy)"/>
      <path d="M0 56 C120 6 250 -4 370 26 L370 44 C250 12 120 24 0 74Z" fill="var(--sky)"/>
      <path d="M0 50 C120 0 250 -10 370 20 L370 26 C250 -4 120 6 0 56Z" fill="var(--white)"/>
    </svg>
    <div class="abs offer">
      <h2>SPECIAL OFFER:</h2>
      <p><b>$69</b> New Patient Special<br><b>$99</b> In-Office Teeth Whitening<br><b>25% - 40%</b> off on clear aligners</p>
    </div>
    <div class="footer">www.brightharborclinic.com</div>
    <div class="footer-under" style="background:var(--navy)"></div>
  </div>
</section>

<section class="spread outside">
  <div class="panel p1 promos">
    <svg class="waves" style="top:0" width="360" height="95" viewBox="0 0 360 95" preserveAspectRatio="none">
      <path d="M0 0 L360 0 L360 70 C240 95 110 40 0 20Z" fill="var(--mist)"/>
      <path d="M0 0 L360 0 L360 55 C240 80 110 25 0 8Z" fill="var(--bright)"/>
      <path d="M0 0 L300 0 C240 30 110 10 0 2Z" fill="var(--sky)"/>
    </svg>
    <div class="abs center" style="top:132px"><div class="section-title"><i></i>OUR PROMOS</div><div class="rule"></div></div>
    <div class="abs promo-box" style="top:197px"><div class="lead"><b>$69</b> New Patients Special</div><div class="sub">Exam, Cleanup, Digital XRays.</div><div class="big">Regular Price $500</div></div>
    <div class="abs promo-box" style="top:319px"><div class="lead"><b>$99</b> In-office<br>teeth Whitening</div><div class="big">Regular Price $700</div></div>
    <div class="abs promo-box" style="top:438px"><div class="lead"><b>25-40%</b> off on clear aligners</div><div class="big">Plus Free Consultation!</div></div>
    <div class="abs center" style="top:560px"><div class="section-title"><i></i>OUR SERVICES</div><div class="rule"></div></div>
    <ul class="abs services">
      <li>Cleaning and Prevention</li><li>Cosmetic Dentistry</li><li>Implant Dentistry</li><li>Removable Dentures</li><li>Orthodontics</li><li>Clear Aligners</li><li>Pediatric Dentistry</li><li>Multi-specialty Treatment</li>
    </ul>
    <div class="abs team-photo" role="img" aria-label="Photo of a smiling group of young women"></div>
    <div class="footer">www.brightharborclinic.com</div>
  </div>

  <div class="panel p2 plan">
    <svg class="waves" style="top:0" width="355" height="80" viewBox="0 0 355 80" preserveAspectRatio="none">
      <path d="M0 0 L355 0 L355 40 C240 70 110 20 0 60Z" fill="var(--mist)"/>
      <path d="M0 0 L355 0 L355 22 C240 52 110 4 0 40Z" fill="var(--pale)"/>
    </svg>
    <div class="abs boxed" style="top:88px;padding:6px 0">PAYMENT<br>OPTIONS AVAILABLE!</div>
    <div class="abs boxed" style="top:187px;padding:6px 0">FINANCING<br>OPTIONS AVAILABLE!</div>
    <div class="abs center note" style="top:290px">Most insurances accepted!<br>No insurance? Try our</div>
    <div class="abs center plan-head" style="top:328px">DENTAL SAVINGS PLAN</div>
    <div class="abs row" style="top:360px"><div class="items">Preventative Exam<br>X-Ray Professional<br>Cleanup</div><div class="brace">}</div><div class="save">80% - 100%<br>Savings</div></div>
    <div class="abs row" style="top:430px"><div class="items">Filling<br>Crowns</div><div class="brace">}</div><div class="save">40% - 80%<br>Savings</div></div>
    <div class="abs boxed plan-head" style="top:503px;padding:8px 0;color:var(--pale)">IN-OFFICE WHITENING</div>
    <div class="abs row" style="top:566px"><div class="items">Advanced Dentures<br>Extractions</div><div class="brace">}</div><div class="save">25%<br>Savings</div></div>
    <div class="abs row" style="top:634px"><div class="items">Braces<br>( Orthodontics )</div><div class="brace">}</div><div class="save">65%<br>Savings</div></div>
    <div class="abs fee"><b>ANNUAL FEE :</b><br>$138 First family member<br>= 11.5/month</div>
    <div class="footer">www.brightharborclinic.com</div>
  </div>

  <div class="panel p3 info">
    <svg class="waves" style="top:0" width="370" height="70" viewBox="0 0 370 70" preserveAspectRatio="none">
      <path d="M0 0 L370 0 L370 60 C300 10 200 0 0 0Z" fill="var(--bright)"/>
      <path d="M120 0 L370 0 L370 30 C300 0 220 -2 120 0Z" fill="var(--sky)"/>
    </svg>
    <div class="abs center brand" style="top:82px;font-size:21px"><span class="brand-mark"></span>THE BRIGHT HARBOR CLINIC</div>
    <div class="abs center hours-title">CONVENIENT<br>SATURDAY HOURS!</div>
    <div class="abs center hours">Tue, Thurs <b>9:30am - 5:00pm</b><br>Fri, Sat <b>9:00am - 5:00pm</b></div>
    <div class="abs center calltoday">CALL US TODAY!<span>555-014-2277</span></div>
    <div class="abs center addr">240 HARBOR LANE SUITE 12<br>BAYVIEW, MA 01999</div>
    <div class="abs center site">www.brightharborclinic.com</div>
    <div class="abs map" role="img" aria-label="Street map showing the clinic location"></div>
    <div class="footer">www.brightharborclinic.com</div>
  </div>
</section>

</body>
</html>
```